Web Instant Messenger Design Project

Hello,
The project consist of designing a web instant messenger interface. What we need is a Photoshop file that contains the design elements of this app. (windows, buttons , dropdowns etc)
notes:
- we are looking for the same look and feel as the now closed Tolvia.com
- the name of the app will be quorind.com , or similar.
- the application will be browser based, will cover 100% of the browser area.
- please don't make a "flat" background.
I attached 3 screen captures that shows the graphic elements we need :
img1: -
is the login "page" with username and password fields. There are also a connect & disconnect buttons + a register one
img2:
a) We have the classic friend list that shows who is online and their status. The friend list window can be moved and has 7
buttons (down:add friedn, delete friend, create group,change friend group and create conference / up: conference room list
and mass message buttons)
b) There is a conversation window that can be dragged. The conversation window will keep the private conversations and
conferences as a tab bar. Please note the key field area .
c) Mass Message window - here you can select the group and/or friends, write the message and hit send.
img3
a) on friend list window , when you click one of the down button a new , non movable window will appear. In this window you will have actions corresponding to the button you clicked : add/ delete friend , create conference , etc
b) public room window- is a drag-able window with the conferences you can join.
c)the conversation window with a conference selected. There is a invite buddy drop down, a list of participants and the conversations zone. On participants list there will be a kick and ban button.(not present in this capture)
Updates
When submitting a design please try to provide a mock of the "friend list window". Thank you and sorry if this info comes too late.
Industry/Entity Type
Group
Look and feel
Each slider illustrates characteristics of the customer's brand and the style your logo design should communicate.

```html
<!DOCTYPE html>
<html lang="en">
<head>
<meta charset="utf-8">
<title>quorind — Sign In</title>
<link href="https://fonts.googleapis.com/css2?family=Open+Sans:wght@400;600;700&display=swap" rel="stylesheet">
<style>
  :root {
    --bar-dark: #0a5c9e;
    --bar-light: #0e9ddf;
    --bar-edge: #0b5f9c;
    --page-bg: #efefef;
    --card-bg: #fafafa;
    --card-border: #d6d6d6;
    --heading: #2b3a4a;
    --muted: #666a6e;
    --field-border: #c9c9c9;
    --addon-bg: #f3f3f3;
    --icon: #8c8c8c;
    --placeholder: #8a8a8a;
    --primary-top: #5a9bd6;
    --primary-bottom: #2f6fb0;
    --primary-border: #2a64a0;
    --light-top: #fbfbfb;
    --light-bottom: #e3e3e3;
    --dark-top: #5e5e5e;
    --dark-bottom: #3a3a3a;
    --brand-mark: #f5b400;
    --white: #ffffff;
  }
  * { box-sizing: border-box; margin: 0; padding: 0; }
  html, body { width: 1200px; height: 700px; overflow: hidden; }
  body {
    font-family: "Open Sans", Arial, sans-serif;
    background: var(--page-bg);
    position: relative;
  }
  .top-bar {
    height: 37px;
    background: linear-gradient(90deg, var(--bar-dark) 0%, var(--bar-light) 50%, var(--bar-dark) 100%);
    border-bottom: 2px solid var(--bar-edge);
    display: flex;
    align-items: center;
    padding-left: 98px;
  }
  .brand { display: flex; align-items: center; gap: 8px; }
  .brand-dot { width: 20px; height: 20px; background: var(--brand-mark); border-radius: 50%; }
  .brand-name { color: var(--white); font-size: 25px; font-weight: 600; letter-spacing: 0.2px; line-height: 1; }
  .signin-card {
    position: absolute;
    left: 409px; top: 142px;
    width: 382px; height: 356px;
    background: var(--card-bg);
    border: 1px solid var(--card-border);
    padding: 20px 30px 0 28px;
  }
  .signin-title { font-size: 25px; font-weight: 700; color: var(--heading); line-height: 30px; }
  .signin-note { font-size: 12px; color: var(--muted); margin-top: 16px; }
  .field {
    display: flex; height: 41px; margin-top: 25px;
    border: 1px solid var(--field-border); border-radius: 3px; background: var(--white);
    overflow: hidden;
  }
  .field + .field { margin-top: 17px; }
  .field-addon {
    width: 39px; background: var(--addon-bg); border-right: 1px solid var(--field-border);
    display: flex; align-items: center; justify-content: center;
  }
  .field-input {
    flex: 1; border: none; outline: none; padding-left: 13px;
    font: 12px "Open Sans", Arial, sans-serif; color: var(--heading); background: transparent;
  }
  .field-input::placeholder { color: var(--placeholder); }
  .btn {
    height: 32px; border-radius: 2px; font: 14px "Open Sans", Arial, sans-serif; cursor: pointer;
  }
  .btn-primary {
    display: block; margin: 14px 0 0 auto; width: 108px;
    background: linear-gradient(var(--primary-top), var(--primary-bottom));
    border: 1px solid var(--primary-border); color: var(--white);
  }
  .divider { border: none; border-top: 1px dotted #cfcfcf; margin-top: 21px; }
  .secondary-actions { display: flex; gap: 9px; margin-top: 21px; }
  .btn-light {
    width: 108px; background: linear-gradient(var(--light-top), var(--light-bottom));
    border: 1px solid #c4c4c4; color: #444;
  }
  .btn-dark {
    width: 108px; background: linear-gradient(var(--dark-top), var(--dark-bottom));
    border: 1px solid #2e2e2e; color: var(--white);
  }
</style>
</head>
<body>
  <header class="top-bar">
    <div class="brand">
      <span class="brand-dot"></span>
      <span class="brand-name">quorind</span>
    </div>
  </header>

  <form class="signin-card">
    <h1 class="signin-title">Sign In</h1>
    <p class="signin-note">Signin using your registered account:</p>

    <label class="field">
      <span class="field-addon">
        <svg width="14" height="14" viewBox="0 0 14 14" aria-hidden="true">
          <circle cx="7" cy="4" r="3" fill="var(--icon)"/>
          <path d="M1 14 C1 9 3.5 7.5 7 7.5 C10.5 7.5 13 9 13 14 Z" fill="var(--icon)"/>
        </svg>
      </span>
      <input class="field-input" type="text" placeholder="Username">
    </label>

    <label class="field">
      <span class="field-addon">
        <svg width="15" height="15" viewBox="0 0 15 15" aria-hidden="true">
          <circle cx="10" cy="5" r="4" fill="var(--icon)"/>
          <circle cx="11" cy="4" r="1.2" fill="var(--addon-bg)"/>
          <path d="M7.5 6.5 L1.5 12.5 L2.5 14 L4 12.5 L5 13.5 L6 12.5 L5 11.5 L9 7.5 Z" fill="var(--icon)"/>
        </svg>
      </span>
      <input class="field-input" type="password" placeholder="Password">
    </label>

    <button class="btn btn-primary" type="button">Connect</button>

    <hr class="divider">

    <div class="secondary-actions">
      <button class="btn btn-light" type="button">Register</button>
      <button class="btn btn-dark" type="button">Disconnect</button>
    </div>
  </form>
</body>
</html>
```